Modern Yoga Studio Timetable and Flyer Design

We have a comprehensive class timetable and we are wanting to a clean modern look for our Spring timetable.

We require a double sided flyer with our class timetable included.
We would prefer an A5 size (postcard) or DL (1/3 A4).

We would like the final flyer to have.
Side A : Yoga image, logo

Fennel Stretch Hall
address: 4/71 Wexcombe Lane, Pelharton
website: fennelstretch.com.au
mobile: 0471 296 814

Side B: Clear easy to read timetable with a break down of class types and website.

We would also like to have a copy of the timetable itself as a separate jpg or pdf for use on our website to download.

Thank you.
Yours kindly,
Nell

I have attached a sample of another timetable of which I like the look and feel of, however this is just a guide. I've also attached our 'new' schedule in WORD plus uploaded our last design of the front.
Updates

Target Market(s)

Women aged 30-45

Industry/Entity Type

Health And Wellness

Font styles to use
Other font styles liked:
• Brandon Grotesque, Jenna Sue

Colors
6c459b
33a6d7
ffffff

Requirements
Must have
• A definitive colour to decipher between different class types on our timetable. Where each colour represents a different class type. Colours and layouts similar to our website design, see www.fennelstretch.com.au
Nice to have
• I've included a design of another studio whose timetable design I like. One of our own yoga images instead of a stock image.
Should not have
• No dark gridlines between the cells/boxes in the timetables. Please don't use stock yoga images.

```html
<!DOCTYPE html>
<html lang="en">
<head>
<meta charset="utf-8">
<title>Fennel Stretch Hall – Class Timetable</title>
<link rel="stylesheet" href="https://fonts.googleapis.com/css2?family=Signika:wght@300;400;600;700&display=swap">
<style>
  :root {
    --ink: #555558;
    --paper: #ffffff;
    --mandala: #e9e7f1;
    --slow-flow: #b9a6d6;      --slow-flow-fill: #7e6aa3;
    --pregnancy: #c6e6a2;      --pregnancy-fill: #9fd585;
    --vinyasa: #f6ab96;        --vinyasa-fill: #d9806a;
    --rise-shine: #d6d6d6;     --rise-shine-fill: #bdb3ae;
    --mum-baby: #a7d9ef;       --mum-baby-fill: #6cb2cf;
    --kids-older: #fbcb97;     --kids-older-fill: #efae6e;
    --teens: #cf9ec6;          --teens-fill: #b46a95;
    --yin-restore: #e8d4be;    --yin-restore-fill: #ad977e;
    --kids-young: #eff08e;     --kids-young-fill: #d4e26b;
    --womens: #a6dfc4;         --womens-fill: #5aa888;
    --flow-restore: #f6ea8c;   --flow-restore-fill: #e3d45e;
    --yin: #f49ac6;            --yin-fill: #c86aa0;
  }
  * { box-sizing: border-box; margin: 0; padding: 0; }
  html, body { width: 1200px; height: 846px; overflow: hidden; background: var(--paper); }
  body { font-family: "Signika", sans-serif; }
  .timetable { position: relative; width: 1200px; height: 846px; overflow: hidden; }

  .mandala { position: absolute; border-radius: 50%;
    background: radial-gradient(circle, rgba(233,231,241,0.15) 30%, rgba(233,231,241,0.75) 62%, rgba(233,231,241,0) 72%); }
  .mandala--top { left: 0; top: -190px; width: 420px; height: 420px; }
  .mandala--bottom { left: 700px; top: 660px; width: 540px; height: 540px; }

  .stem { position: absolute; width: 3px; bottom: 82px; background: var(--c); }
  .stem--top { top: 108px; }
  .stem--low { top: 252px; }

  .class-badge { position: absolute; width: 144px; height: 144px; margin: -72px 0 0 -72px; border-radius: 50%; }
  .class-badge__photo { position: absolute; inset: 0; border-radius: 50%; background: var(--f); opacity: 0.92; }
  .class-badge__name { position: absolute; inset: 0; display: flex; flex-direction: column; align-items: center; justify-content: center;
    color: #fff; font-weight: 700; text-align: center; line-height: 0.9; font-size: 30px; letter-spacing: 0.5px; }
  .class-badge__name small { font-size: 18px; line-height: 0.8; }
  .class-badge__star { position: absolute; top: 6px; left: 0; right: 0; text-align: center; color: #fff; font-size: 28px; font-weight: 700; line-height: 1; }

  .day { position: absolute; left: 35px; font-size: 31px; font-weight: 600; color: var(--ink); letter-spacing: 1px; line-height: 1; transform: translateY(-50%); }

  .time { position: absolute; color: var(--c); font-weight: 600; font-size: 27px; line-height: 0.86; }
  .time--pair { font-size: 18px; line-height: 1.12; margin-top: 5px; }

  .note { position: absolute; left: 35px; top: 788px; font-size: 21px; font-weight: 300; color: var(--ink); letter-spacing: 0.3px; }
  .site { position: absolute; right: 36px; top: 788px; font-size: 21px; font-weight: 400; color: #333; }
</style>
</head>
<body>
<main class="timetable">
  <div class="mandala mandala--top" role="img" aria-label="Faint decorative mandala pattern"></div>
  <div class="mandala mandala--bottom" role="img" aria-label="Faint decorative mandala pattern"></div>

  <!-- stems -->
  <div class="stem stem--top" style="left:136px;--c:var(--slow-flow)"></div>
  <div class="stem stem--low" style="left:225px;--c:var(--pregnancy)"></div>
  <div class="stem stem--top" style="left:312px;--c:var(--vinyasa)"></div>
  <div class="stem stem--low" style="left:398px;--c:var(--rise-shine)"></div>
  <div class="stem stem--top" style="left:486px;--c:var(--mum-baby)"></div>
  <div class="stem stem--low" style="left:572px;--c:var(--kids-older)"></div>
  <div class="stem stem--top" style="left:659px;--c:var(--teens)"></div>
  <div class="stem stem--low" style="left:746px;--c:var(--yin-restore)"></div>
  <div class="stem stem--top" style="left:833px;--c:var(--kids-young)"></div>
  <div class="stem stem--low" style="left:919px;--c:var(--womens)"></div>
  <div class="stem stem--top" style="left:1006px;--c:var(--flow-restore)"></div>
  <div class="stem stem--low" style="left:1092px;--c:var(--yin)"></div>

  <!-- class badges, top row -->
  <div class="class-badge" style="left:138px;top:108px;--f:var(--slow-flow-fill)">
    <div class="class-badge__photo" role="img" aria-label="Photo of a slow flow yoga pose"></div>
    <div class="class-badge__name">SLOW<br>FLOW</div>
  </div>
  <div class="class-badge" style="left:314px;top:108px;--f:var(--vinyasa-fill)">
    <div class="class-badge__photo" role="img" aria-label="Photo of a vinyasa flow class"></div>
    <div class="class-badge__name" style="font-size:26px">VINYASA<br>FLOW</div>
  </div>
  <div class="class-badge" style="left:488px;top:108px;--f:var(--mum-baby-fill)">
    <div class="class-badge__photo" role="img" aria-label="Photo of a mum and baby yoga class"></div>
    <span class="class-badge__star">*</span>
    <div class="class-badge__name" style="font-size:29px">MUM<br><small>+</small><br>BABY</div>
  </div>
  <div class="class-badge" style="left:661px;top:108px;--f:var(--teens-fill)">
    <div class="class-badge__photo" role="img" aria-label="Photo of a teens yoga class"></div>
    <span class="class-badge__star">*</span>
    <div class="class-badge__name">TEENS<br>12-16</div>
  </div>
  <div class="class-badge" style="left:834px;top:108px;--f:var(--kids-young-fill)">
    <div class="class-badge__photo" role="img" aria-label="Photo of a young child doing yoga"></div>
    <span class="class-badge__star">*</span>
    <div class="class-badge__name">KIDS<br>5-7</div>
  </div>
  <div class="class-badge" style="left:1008px;top:108px;--f:var(--flow-restore-fill)">
    <div class="class-badge__photo" role="img" aria-label="Photo of a flow and restore class"></div>
    <div class="class-badge__name" style="font-size:25px">FLOW<br><small>+</small><br>RESTORE</div>
  </div>

  <!-- class badges, lower row -->
  <div class="class-badge" style="left:226px;top:252px;--f:var(--pregnancy-fill)">
    <div class="class-badge__photo" role="img" aria-label="Photo of a pregnancy yoga pose"></div>
    <span class="class-badge__star">*</span>
    <div class="class-badge__name" style="font-size:20px">PREGNANCY</div>
  </div>
  <div class="class-badge" style="left:400px;top:252px;--f:var(--rise-shine-fill)">
    <div class="class-badge__photo" role="img" aria-label="Photo of a morning yoga class"></div>
    <span class="class-badge__star">*</span>
    <div class="class-badge__name" style="font-size:29px">RISE<br><small>+</small><br>SHINE</div>
  </div>
  <div class="class-badge" style="left:574px;top:252px;--f:var(--kids-older-fill)">
    <div class="class-badge__photo" role="img" aria-label="Photo of children doing yoga"></div>
    <span class="class-badge__star">*</span>
    <div class="class-badge__name">KIDS<br>8-12</div>
  </div>
  <div class="class-badge" style="left:747px;top:252px;--f:var(--yin-restore-fill)">
    <div class="class-badge__photo" role="img" aria-label="Photo of a restorative yoga class"></div>
    <div class="class-badge__name" style="font-size:26px">YIN<br><small>+</small><br>RESTORE</div>
  </div>
  <div class="class-badge" style="left:921px;top:252px;--f:var(--womens-fill)">
    <div class="class-badge__photo" role="img" aria-label="Photo of a women's wellness class"></div>
    <span class="class-badge__star">*</span>
    <div class="class-badge__name" style="font-size:22px">WOMEN'S<br>WELLNESS</div>
  </div>
  <div class="class-badge" style="left:1094px;top:252px;--f:var(--yin-fill)">
    <div class="class-badge__photo" role="img" aria-label="Photo of a yin yoga class"></div>
    <div class="class-badge__name">YIN</div>
  </div>

  <!-- days -->
  <div class="day" style="top:373px">MON</div>
  <div class="day" style="top:437px">TUE</div>
  <div class="day" style="top:499px">WED</div>
  <div class="day" style="top:562px">THU</div>
  <div class="day" style="top:626px">FRI</div>
  <div class="day" style="top:689px">SAT</div>
  <div class="day" style="top:752px">SUN</div>

  <!-- slow flow -->
  <div class="time" style="left:147px;top:343px;--c:var(--slow-flow)">9:30<br>AM</div>
  <div class="time" style="left:147px;top:469px;--c:var(--slow-flow)">6:00<br>PM</div>
  <!-- pregnancy -->
  <div class="time" style="left:233px;top:343px;--c:var(--pregnancy)">6:00<br>PM</div>
  <div class="time" style="left:233px;top:407px;--c:var(--pregnancy)">7:30<br>PM</div>
  <div class="time time--pair" style="left:233px;top:532px;--c:var(--pregnancy)">12:15PM<br>6:15PM</div>
  <div class="time" style="left:233px;top:659px;--c:var(--pregnancy)">10:30<br>AM</div>
  <!-- vinyasa -->
  <div class="time" style="left:322px;top:343px;--c:var(--vinyasa)">7:30<br>PM</div>
  <div class="time time--pair" style="left:322px;top:407px;--c:var(--vinyasa)">9:15AM<br>6:00PM</div>
  <div class="time" style="left:322px;top:532px;--c:var(--vinyasa)">9:30<br>AM</div>
  <div class="time time--pair" style="left:322px;top:659px;--c:var(--vinyasa)">9:00AM<br>4:00PM</div>
  <!-- rise + shine -->
  <div class="time" style="left:409px;top:407px;--c:var(--rise-shine)">5:45<br>AM</div>
  <div class="time" style="left:409px;top:532px;--c:var(--rise-shine)">5:45<br>AM</div>
  <!-- mum + baby -->
  <div class="time" style="left:496px;top:407px;--c:var(--mum-baby)">11:00<br>AM</div>
  <div class="time" style="left:496px;top:532px;--c:var(--mum-baby)">11:00<br>AM</div>
  <!-- kids 8-12 -->
  <div class="time" style="left:581px;top:469px;--c:var(--kids-older)">4:00<br>PM</div>
  <!-- teens -->
  <div class="time" style="left:669px;top:469px;--c:var(--teens)">4:45<br>PM</div>
  <div class="time" style="left:669px;top:532px;--c:var(--teens)">5:00<br>PM</div>
  <!-- yin + restore -->
  <div class="time" style="left:755px;top:469px;--c:var(--yin-restore)">7:30<br>PM</div>
  <!-- kids 5-7 -->
  <div class="time" style="left:842px;top:532px;--c:var(--kids-young)">4:00<br>PM</div>
  <!-- women's wellness -->
  <div class="time" style="left:928px;top:532px;--c:var(--womens)">7:30<br>PM</div>
  <!-- flow + restore -->
  <div class="time" style="left:1015px;top:596px;--c:var(--flow-restore)">6:00<br>PM</div>
  <!-- yin -->
  <div class="time" style="left:1102px;top:722px;--c:var(--yin)">9:15<br>AM</div>

  <p class="note">*BOOKINGS ESSENTIAL</p>
  <p class="site">www.fennelstretch.com.au</p>
</main>
</body>
</html>
```